I need a new business card design for my pharmacy.

I need a business card design. I will include my logo.
The card needs to be readable. I prefer to have my logo on one side along with my website, the other side includes the other information. Please use combination of black, neon green, white, and silver. This needs to catch the eye but yet be clearly visible and legible. Thanks

Industry/Entity Type

Pharmacy

Contact Information for Business Card

It needs to have the following information listed:
Vel's Apothecary Owner/Pharm D.
7143 North Birch Lane
Sioux Falls, SD 57362
Phone 605-318-6027
Fax 605-318-6025
email: vel@velsapothecary.example
www.velsapothecary.example
Store hours Monday-Friday 8 am- 7 pm
Saturday 8 am- 12 pm
Sunday Closed
Please utilize the colors black, white, and neon green, maybe silver.

Requirements
Must have
• It needs to be easily readable!
Nice to have
• It should catch the eye.
Should not have
• Do not use any other colors except listed: black, neon green, white, & silver.

```html
<!DOCTYPE html>
<html lang="en">
<head>
<meta charset="utf-8">
<title>Vel's Apothecary – Business Card</title>
<link rel="stylesheet" href="https://fonts.googleapis.com/css2?family=Open+Sans:wght@400;600;700&display=swap">
<style>
  :root {
    --neon: #8fd13a;
    --neon-light: #c4e86e;
    --ink: #111111;
    --ink-soft: #2b2b2b;
    --white: #ffffff;
    --silver-top: #e4ebf0;
    --silver-bottom: #a9b9c6;
    --stage: #e9eaec;
  }
  * { box-sizing: border-box; margin: 0; padding: 0; }
  html, body { width: 1200px; height: 913px; overflow: hidden; }
  body {
    background: var(--stage);
    font-family: "Open Sans", Arial, sans-serif;
    color: var(--ink);
    position: relative;
  }
  .card {
    position: absolute;
    top: 300px;
    width: 540px;
    height: 310px;
    overflow: hidden;
    box-shadow: 0 6px 18px rgba(0,0,0,.18);
  }
  /* ---------- contact side ---------- */
  .card--contact {
    left: 30px;
    background: linear-gradient(200deg, var(--neon-light) 0%, var(--neon) 55%, #79bf26 100%);
  }
  .dots { position: absolute; top: 0; right: 0; }
  .hours {
    position: absolute; left: 26px; top: 24px;
    list-style: none; font-size: 15px; line-height: 20px; color: var(--ink-soft);
  }
  .hours li { display: flex; align-items: center; gap: 8px; }
  .hours svg { flex: none; }
  .rule {
    position: absolute; left: 26px; right: 26px; top: 78px;
    height: 1px; background: var(--ink-soft); opacity: .7;
  }
  .address {
    position: absolute; right: 28px; top: 92px;
    text-align: right; font-size: 14px; line-height: 19px; color: var(--ink-soft);
  }
  .brand {
    position: absolute; left: 26px; top: 132px;
    display: flex; align-items: center; gap: 14px;
  }
  .brand__dot { width: 26px; height: 26px; border-radius: 50%; background: var(--ink); }
  .brand__divider { width: 1px; height: 40px; background: var(--ink-soft); }
  .brand__name { font-size: 27px; font-weight: 700; letter-spacing: -.5px; color: var(--ink-soft); }
  .person { position: absolute; left: 26px; top: 196px; }
  .person__name { font-size: 20px; font-weight: 700; color: var(--ink); line-height: 24px; }
  .person__title { font-size: 15px; color: var(--white); line-height: 20px; }
  .contacts {
    position: absolute; left: 30px; top: 246px;
    list-style: none; font-size: 14px; line-height: 18px; color: var(--ink);
  }
  .contacts li { display: flex; align-items: center; gap: 8px; }
  .corner { position: absolute; right: 0; bottom: 0; }

  /* ---------- logo side ---------- */
  .card--logo {
    left: 630px;
    background: linear-gradient(170deg, var(--silver-top) 0%, #c6d3dc 55%, var(--silver-bottom) 100%);
  }
  .card--logo .brand { left: 60px; top: 108px; gap: 20px; }
  .card--logo .brand__dot { width: 40px; height: 40px; }
  .card--logo .brand__divider { height: 60px; }
  .card--logo .brand__name { font-size: 38px; color: var(--ink-soft); }
  .website {
    position: absolute; left: 210px; top: 206px;
    display: flex; align-items: center; gap: 8px;
    font-size: 15px; color: var(--ink-soft);
  }
  .website__dot { width: 9px; height: 9px; border-radius: 50%; background: var(--neon); }
</style>
</head>
<body>

<section class="card card--contact">
  <svg class="dots" width="260" height="150" viewBox="0 0 260 150" aria-hidden="true">
    <g fill="#ffffff" opacity=".3">
      <ellipse cx="80" cy="22" rx="26" ry="17"/>
      <ellipse cx="130" cy="58" rx="26" ry="17"/>
      <ellipse cx="195" cy="48" rx="26" ry="17"/>
      <ellipse cx="236" cy="70" rx="26" ry="17"/>
      <ellipse cx="180" cy="105" rx="26" ry="17"/>
      <ellipse cx="232" cy="135" rx="26" ry="17"/>
    </g>
  </svg>

  <ul class="hours">
    <li><svg width="11" height="10" viewBox="0 0 11 10"><path d="M1 5l3 3 6-7" fill="none" stroke="#fff" stroke-width="2"/></svg>Store hours Monday-Friday 8 am - 7 pm</li>
    <li><svg width="11" height="10" viewBox="0 0 11 10"><path d="M1 5l3 3 6-7" fill="none" stroke="#fff" stroke-width="2"/></svg>Saturdays 8 am - 12 pm, Sundays closed</li>
  </ul>
  <div class="rule"></div>

  <address class="address" style="font-style:normal">
    7143 North Birch Lane<br>Sioux Falls, SD 57362
  </address>

  <div class="brand">
    <span class="brand__dot"></span>
    <span class="brand__divider"></span>
    <span class="brand__name">Vel's Apothecary</span>
  </div>

  <div class="person">
    <p class="person__name">Vel's Apothecary</p>
    <p class="person__title">Owner/Pharm D</p>
  </div>

  <ul class="contacts">
    <li><svg width="11" height="11" viewBox="0 0 24 24"><path fill="#fff" d="M6.6 10.8a15 15 0 006.6 6.6l2.2-2.2c.3-.3.7-.4 1-.2 1.1.4 2.3.6 3.6.6.6 0 1 .4 1 1V20c0 .6-.4 1-1 1A17 17 0 013 4c0-.6.4-1 1-1h3.5c.6 0 1 .4 1 1 0 1.3.2 2.5.6 3.6.1.3 0 .7-.2 1z"/></svg>605-318-6027</li>
    <li><svg width="11" height="11" viewBox="0 0 24 24"><path fill="#fff" d="M6 3h10v5H6zM3 9h18v9h-3v3H6v-3H3zm5 7v3h8v-3z"/></svg>605-318-6025</li>
    <li><svg width="11" height="9" viewBox="0 0 22 16"><rect x="1" y="1" width="20" height="14" fill="none" stroke="#fff" stroke-width="2"/><path d="M1 1l10 8 10-8" fill="none" stroke="#fff" stroke-width="2"/></svg>vel@velsapothecary.example</li>
  </ul>

  <svg class="corner" width="190" height="80" viewBox="0 0 190 80" aria-hidden="true">
    <polygon points="60,80 120,0 190,0 190,80" fill="#ffffff"/>
    <polygon points="92,80 152,0 170,0 110,80" fill="#111111"/>
    <polygon points="0,80 60,80 70,66 10,66" fill="#111111"/>
  </svg>
</section>

<section class="card card--logo">
  <div class="brand">
    <span class="brand__dot"></span>
    <span class="brand__divider"></span>
    <span class="brand__name">Vel's Apothecary</span>
  </div>
  <p class="website"><span class="website__dot"></span>www.velsapothecary.example</p>
</section>

</body>
</html>
```